Powerpoint template & style design project

KLavender Consulting is an IT technology firm specializing in mobility and telecommunications applications. We provide technical consulting to global companies that want to build mobile applications and take critical business applications and move them into the cloud.
We would like to see designs that use the color blue. The final design should communicate confidence, agility and speak to technology focused customers. Forward progress and/or motion should be conveyed.

Target Market(s)

Government customers and large enterprise companies

Industry/Entity Type

Telecommunications

Font styles to use
Sans Serif

Colors
0555a3

Requirements
Must have
• different slides: Cover page, title slide, main content, transition slide, close out slide..

```html
<!DOCTYPE html>
<html lang="en">
<head>
<meta charset="utf-8">
<title>KLavender Consulting – Presentation Template</title>
<link href="https://fonts.googleapis.com/css2?family=Open+Sans:wght@400;600;700;800&display=swap" rel="stylesheet">
<style>
  :root{
    --brand:#0555a3;
    --brand-light:#4a8fd0;
    --brand-deep:#0a4c94;
    --ink:#3a3a3a;
    --muted:#6b6b6b;
    --rule:#4a4a4a;
    --band:#d5d5d5;
    --bar-dark:#3d3d3d;
    --stage:#2f2f2f;
    --paper:#ffffff;
    --green:#8cb64a;
    --blue:#2f80c3;
    --navy:#2a3b55;
  }
  *{box-sizing:border-box;margin:0;padding:0}
  html,body{width:1000px;height:1200px;overflow:hidden;background:var(--stage)}
  body{font-family:"Open Sans",Arial,sans-serif;color:var(--ink)}
  .canvas{position:relative;width:1000px;height:1200px}
  .slide{position:absolute;width:457px;height:342px;background:var(--paper);overflow:hidden}
  .s-cover{left:28px;top:57px}
  .s-intro{left:515px;top:57px}
  .s-text{left:28px;top:430px}
  .s-charts{left:515px;top:430px}
  .s-section{left:28px;top:803px;background:var(--brand)}
  .s-contact{left:515px;top:803px}

  /* cover */
  .cover-band{position:absolute;left:10px;top:8px;width:438px;height:198px;background:linear-gradient(100deg,var(--brand) 0%,#1462b0 100%)}
  .cover-title{position:absolute;left:15px;top:92px;color:#fff;font-weight:700;font-size:18.5px;line-height:24px}
  .cover-sub{position:absolute;left:15px;top:143px;color:#fff;font-size:13px}
  .cover-date{position:absolute;left:15px;top:173px;color:#fff;font-size:11.5px}
  .brand-name{font-family:"Open Sans",Arial,sans-serif;font-weight:700;color:var(--brand);white-space:nowrap;display:flex;align-items:center;gap:5px}
  .brand-name .dot{display:inline-block;background:currentColor}
  .cover-brand{position:absolute;left:25px;top:243px;font-size:15px}
  .cover-brand .dot{width:10px;height:10px}
  .cover-bar{position:absolute;left:10px;top:318px;width:438px;height:14px;background:var(--bar-dark)}

  /* headings */
  .slide-heading{position:absolute;left:0;width:100%;top:4px;text-align:center;font-size:15.5px;font-weight:700;color:var(--brand);letter-spacing:.2px}
  .slide-heading .sub{font-weight:400;color:var(--brand-light)}
  .heading-rule{position:absolute;left:50%;top:29px;width:90px;height:2px;margin-left:-45px;background:var(--rule)}

  /* footer */
  .footer{position:absolute;left:0;bottom:0;width:100%;height:28px;background:var(--band)}
  .footer-brand{position:absolute;left:12px;top:9px;font-size:6.5px}
  .footer-brand .dot{width:5px;height:5px}
  .footer-copy{position:absolute;left:0;width:100%;top:10px;text-align:center;font-size:5.5px;color:var(--muted)}
  .footer-slash{position:absolute;right:0;bottom:0}
  .footer-num{position:absolute;right:15px;top:9px;font-size:7px;font-weight:700;color:var(--brand)}

  /* intro */
  .intro-photo{position:absolute;left:13px;top:40px;width:431px;height:146px;background:linear-gradient(110deg,#2a6fb8 0%,#3b82c8 45%,#5a97d2 60%,#2c6db4 100%)}
  .intro-copy{position:absolute;left:13px;top:200px;width:255px;font-size:9.6px;line-height:15px;color:#555}

  /* text slide */
  .pull-quote{position:absolute;left:17px;top:72px;width:110px;font-size:6.2px;line-height:10px;font-weight:700;font-style:italic;color:var(--brand);text-align:justify}
  .text-col{position:absolute;top:72px;width:140px;height:192px;overflow:hidden;font-size:6px;line-height:10.2px;color:#666;text-align:justify}
  .text-col p+p{margin-top:10px;text-indent:12px}
  .col-a{left:147px}
  .col-b{left:300px}

  /* charts */
  .chart{position:absolute}
  .chart-bar{left:12px;top:80px}
  .chart-pie{left:262px;top:80px}
  .chart-divider{position:absolute;left:233px;top:75px;width:1px;height:178px;background:#ddd}
  .chart-title{position:absolute;font-size:8.6px;color:#555}
  .chart-note{position:absolute;width:160px;font-size:6.2px;line-height:9.5px;color:#555}
  .ct1{left:44px;top:210px}.cn1{left:44px;top:225px}
  .ct2{left:270px;top:210px}.cn2{left:270px;top:225px}
  .legend{position:absolute;font-size:5.6px;color:#555;line-height:11px}
  .legend span{display:inline-block;width:5px;height:5px;margin-right:3px;vertical-align:middle}
  .lg1{left:180px;top:125px}.lg2{left:389px;top:125px}

  /* section */
  .section-photo{position:absolute;inset:0;background:radial-gradient(ellipse at 30% 25%,#3a7fca 0%,#1f66b3 40%,var(--brand) 80%)}
  .section-brand{position:absolute;left:18px;top:172px;font-size:16px;color:#fff}
  .section-brand .dot{width:10px;height:10px}
  .section-slash{position:absolute;left:203px;top:165px}
  .section-label{position:absolute;left:238px;top:177px;color:#fff;font-weight:700;font-size:13.5px}

  /* contact */
  .contact-map{position:absolute;left:12px;top:40px;width:430px;height:146px;background:linear-gradient(160deg,#c9c9c9 0%,#b5b5b5 50%,#c3c3c3 100%)}
  .contact-item{position:absolute;display:flex;gap:10px;font-size:10px;line-height:14px;color:var(--brand)}
  .contact-item svg{flex:none;margin-top:1px}
  .ci-addr{left:17px;top:198px;width:200px}
  .ci-phone{left:17px;top:269px}
  .ci-mail{left:248px;top:198px}
  .ci-fb{left:248px;top:226px}
  .ci-tw{left:248px;top:254px}
  .ci-web{left:248px;top:282px}
  .ci-fb .mark,.ci-tw .mark{width:10px;height:10px;border-radius:50%;background:var(--ink);margin-top:2px;flex:none}
</style>
</head>
<body>
<div class="canvas">

  <!-- Cover -->
  <section class="slide s-cover">
    <div class="cover-band"></div>
    <h1 class="cover-title">Insert The Title of Your<br>Presentation Here</h1>
    <p class="cover-sub">Subtitle of the Presentation</p>
    <p class="cover-date">April 12, 2015</p>
    <div class="brand-name cover-brand"><i class="dot"></i>KLavender Consulting</div>
    <div class="cover-bar"></div>
  </section>

  <!-- Introduction -->
  <section class="slide s-intro">
    <h2 class="slide-heading">INTRODUCTION / <span class="sub">ABOUT US</span></h2>
    <div class="heading-rule"></div>
    <div class="intro-photo" role="img" aria-label="Blue-toned photo of a business handshake over a city skyline"></div>
    <p class="intro-copy">Lorem ipsum dolor sit amet, consectetur adipiscing elit, sed do eiusmod tempor incididunt ut labore et dolore magna aliqua. Ut enim ad minim veniam, quis nostrud exercitation ullamco laboris nisi ut aliquip ex ea commodo consequat. Duis aute irure dolor in rep-rehenderit in voluptate velit esse cillum dolore eu fugiat nulla pariatur.</p>
    <footer class="footer">
      <div class="brand-name footer-brand"><i class="dot"></i>KLavender Consulting</div>
      <p class="footer-copy">© 2015 KLavender Consulting. All right reserved.</p>
      <svg class="footer-slash" width="40" height="36" viewBox="0 0 40 36"><line x1="5" y1="36" x2="20" y2="8" stroke="#0555a3" stroke-width="1.2"/></svg>
      <span class="footer-num">2</span>
    </footer>
  </section>

  <!-- Text content -->
  <section class="slide s-text">
    <h2 class="slide-heading">YOUR SAMPLE TITLE / <span class="sub">Your subtitle goes here</span></h2>
    <div class="heading-rule"></div>
    <p class="pull-quote">“Sed ut perspiciatis unde omnis iste natus error sit voluptatem accusantium doloremque laudantium, totam rem aperiam, eaque ipsa quae ab illo inventore veritatis et quasi architecto beatae vitae”</p>
    <div class="text-col col-a">
      <p>Lorem ipsum dolor sit amet, consectetur adipiscing elit sed do eiusmod tempor incididunt ut labore et dolore magna aliqua. Ut enim ad minim veniam, quis nostrud exercitation ullamco laboris nisi ut aliquip ex ea commodo consequat. Duis aute irure dolor in reprehenderit in voluptate velit esse cillum dolore eu fugiat nulla pariatur. Excepteur sint occaecat cupidatat non proident, sunt in culpa qui mollit anim id est laborum.</p>
      <p>Sed ut perspiciatis unde omnis iste natus error sit voluptatem accusantium doloremque laudantium, totam rem aperiam, eaque ipsa quae ab illo inventore veritatis et quasi architecto beatae vitae dicta sunt explicabo. Nemo enim ipsam voluptatem quia voluptas sit aspernatur</p>
    </div>
    <div class="text-col col-b">
      <p>aut odit aut fugit, sed quia consequuntur magni dolores eos qui ratione voluptatem sequi nesciunt. Neque porro quisquam est, qui dolorem ipsum quia dolor sit amet, consectetur, adipisci velit, sed quia non numquam eius modi tempora incidunt ut labore et dolore magnam aliquam quaerat voluptatem. Ut enim ad minima veniam, quis nostrum exercitationem ullam corporis suscipit laboriosam, nisi ut aliquid ex ea commodi consequatur?</p>
      <p>Quis autem vel eum iure reprehenderit qui in ea voluptate velit esse quam nihil molestiae consequatur, vel illum qui dolorem eum fugiat quo voluptas nulla pariatur? At vero eos et</p>
    </div>
    <footer class="footer">
      <div class="brand-name footer-brand"><i class="dot"></i>KLavender Consulting</div>
      <p class="footer-copy">© 2015 KLavender Consulting. All right reserved.</p>
      <svg class="footer-slash" width="40" height="36" viewBox="0 0 40 36"><line x1="5" y1="36" x2="20" y2="8" stroke="#0555a3" stroke-width="1.2"/></svg>
      <span class="footer-num">4</span>
    </footer>
  </section>

  <!-- Charts -->
  <section class="slide s-charts">
    <h2 class="slide-heading">YOUR SAMPLE TITLE / <span class="sub">Your subtitle goes here</span></h2>
    <div class="heading-rule"></div>
    <svg class="chart chart-bar" width="165" height="120" viewBox="0 0 165 120" font-family="Open Sans, sans-serif" font-size="5.5" fill="#555">
      <g stroke="#e3e3e3" stroke-width=".5">
        <line x1="22" y1="105" x2="160" y2="105"/>
        <line x1="22" y1="95.2" x2="160" y2="95.2"/><line x1="22" y1="85.4" x2="160" y2="85.4"/>
        <line x1="22" y1="75.6" x2="160" y2="75.6"/><line x1="22" y1="65.8" x2="160" y2="65.8"/>
        <line x1="22" y1="56" x2="160" y2="56"/><line x1="22" y1="46.2" x2="160" y2="46.2"/>
        <line x1="22" y1="36.4" x2="160" y2="36.4"/><line x1="22" y1="26.6" x2="160" y2="26.6"/>
        <line x1="22" y1="16.8" x2="160" y2="16.8"/>
      </g>
      <g text-anchor="end">
        <text x="18" y="107">0</text><text x="18" y="97">0.5</text><text x="18" y="87">1</text>
        <text x="18" y="78">1.5</text><text x="18" y="68">2</text><text x="18" y="58">2.5</text>
        <text x="18" y="48">3</text><text x="18" y="38">3.5</text><text x="18" y="29">4</text>
        <text x="18" y="19">4.5</text>
      </g>
      <rect x="30" y="20.7" width="9" height="84.3" fill="#8cb64a"/>
      <rect x="40" y="58" width="9" height="47" fill="#2f80c3"/>
      <rect x="50" y="65.8" width="9" height="39.2" fill="#2a3b55"/>
      <rect x="76" y="56" width="9" height="49" fill="#8cb64a"/>
      <rect x="86" y="18.8" width="9" height="86.2" fill="#2f80c3"/>
      <rect x="96" y="65.8" width="9" height="39.2" fill="#2a3b55"/>
      <rect x="122" y="36.4" width="9" height="68.6" fill="#8cb64a"/>
      <rect x="132" y="69.7" width="9" height="35.3" fill="#2f80c3"/>
      <rect x="142" y="46.2" width="9" height="58.8" fill="#2a3b55"/>
      <g text-anchor="middle"><text x="45" y="115">Category 1</text><text x="91" y="115">Category 2</text><text x="137" y="115">Category 3</text></g>
    </svg>
    <div class="legend lg1"><span style="background:var(--green)"></span>Series 1<br><span style="background:var(--blue)"></span>Series 2<br><span style="background:var(--navy)"></span>Series 3</div>
    <div class="chart-divider"></div>
    <svg class="chart chart-pie" width="110" height="110" viewBox="0 0 110 110">
      <circle cx="55" cy="55" r="49" fill="#2a3b55"/>
      <path d="M55 55 L55 6 A49 49 0 0 1 70.1 101.6 Z" fill="#8cb64a"/>
      <path d="M55 55 L70.1 101.6 A49 49 0 0 1 8.4 70.1 Z" fill="#2f80c3"/>
    </svg>
    <div class="legend lg2"><span style="background:var(--green)"></span>Category 1<br><span style="background:var(--blue)"></span>Category 2<br><span style="background:var(--navy)"></span>Category 3</div>
    <h3 class="chart-title ct1">Chart Sample One</h3>
    <p class="chart-note cn1">Lorem ipsum dolor sit amet, consectetur adipiscing elit. Aliquam tincidunt ante nec sem congue convallis lorem ipsum.</p>
    <h3 class="chart-title ct2">Chart Sample Two</h3>
    <p class="chart-note cn2">Lorem ipsum dolor sit amet, consectetur adipiscing elit. Aliquam tincidunt ante nec sem congue convallis lorem ipsum.</p>
    <footer class="footer">
      <div class="brand-name footer-brand"><i class="dot"></i>KLavender Consulting</div>
      <p class="footer-copy">© 2015 KLavender Consulting. All right reserved.</p>
      <svg class="footer-slash" width="40" height="36" viewBox="0 0 40 36"><line x1="5" y1="36" x2="20" y2="8" stroke="#0555a3" stroke-width="1.2"/></svg>
      <span class="footer-num">3</span>
    </footer>
  </section>

  <!-- Section divider -->
  <section class="slide s-section">
    <div class="section-photo" role="img" aria-label="Blue-tinted photo of hands using a mobile device"></div>
    <div class="brand-name section-brand"><i class="dot"></i>KLavender Consulting</div>
    <svg class="section-slash" width="28" height="40" viewBox="0 0 28 40"><line x1="4" y1="38" x2="24" y2="2" stroke="#ffffff" stroke-width="1"/></svg>
    <h2 class="section-label">SECTION TWO</h2>
  </section>

  <!-- Contact -->
  <section class="slide s-contact">
    <h2 class="slide-heading">CONTACT US</h2>
    <div class="heading-rule"></div>
    <div class="contact-map" role="img" aria-label="Grayscale street map showing the office location with a blue pin"></div>
    <div class="contact-item ci-addr">
      <svg width="10" height="12" viewBox="0 0 10 12"><path d="M5 0a4.5 4.5 0 0 0-4.5 4.5C.5 8 5 12 5 12s4.5-4 4.5-7.5A4.5 4.5 0 0 0 5 0z" fill="#0555a3"/><circle cx="5" cy="4.5" r="1.7" fill="#fff"/></svg>
      <span>Lorem ipsum dolor sit amet, consectetur adipiscing elit, sed do eiusmod tempor incididunt ut labore et dolore</span>
    </div>
    <div class="contact-item ci-phone">
      <svg width="11" height="11" viewBox="0 0 11 11"><path d="M2.2 0.5l1.8 2.3-1 1.2c.7 1.6 2 2.9 3.6 3.6l1.2-1 2.3 1.8-.8 1.9C5.2 10.2.8 5.8.3 1.3z" fill="#0555a3"/></svg>
      <span>1234567890</span>
    </div>
    <div class="contact-item ci-mail">
      <svg width="13" height="10" viewBox="0 0 13 10"><rect x=".6" y=".6" width="11.8" height="8.8" fill="none" stroke="#3a3a3a" stroke-width="1.2"/><path d="M.6.8l5.9 4.6L12.4.8" fill="none" stroke="#3a3a3a" stroke-width="1.2"/></svg>
      <span>hello@klavenderconsulting.com</span>
    </div>
    <div class="contact-item ci-fb"><i class="mark"></i><span>klavenderconsulting</span></div>
    <div class="contact-item ci-tw"><i class="mark"></i><span>@klavenderconsult</span></div>
    <div class="contact-item ci-web">
      <svg width="11" height="11" viewBox="0 0 11 11"><circle cx="5.5" cy="5.5" r="4.8" fill="none" stroke="#3a3a3a" stroke-width="1.1"/><ellipse cx="5.5" cy="5.5" rx="2" ry="4.8" fill="none" stroke="#3a3a3a" stroke-width=".8"/><line x1=".7" y1="5.5" x2="10.3" y2="5.5" stroke="#3a3a3a" stroke-width=".8"/></svg>
      <span>www.klavenderconsulting.com</span>
    </div>
    <footer class="footer">
      <div class="brand-name footer-brand"><i class="dot"></i>KLavender Consulting</div>
      <p class="footer-copy">© 2015 KLavender Consulting. All right reserved.</p>
      <svg class="footer-slash" width="40" height="36" viewBox="0 0 40 36"><line x1="5" y1="36" x2="20" y2="8" stroke="#0555a3" stroke-width="1.2"/></svg>
      <span class="footer-num">5</span>
    </footer>
  </section>

</div>
</body>
</html>
```